Card and letterhead for a financial planning firm
Bright Harbor Associates
Professional
Neil Vardakian
Senior Account Executive
4780 W. Meadow Rd
State College, PA 16934
neil@brightharborpa.example
www.brightharborpa.example
I prefer to have a larger font, I don't like cards that make you squint to read the info.
the logo
Please use this logo. Don't be afraid to change the layout of the logo if it enhances the design as in placing the logo next to the name vs. over it.

```html
<!DOCTYPE html>
<html lang="en">
<head>
<meta charset="utf-8">
<title>Bright Harbor Associates — Stationery</title>
<link href="https://fonts.googleapis.com/css2?family=Montserrat:wght@400;600;800&display=swap" rel="stylesheet">
<style>
  :root{
    --bg:#e9e7e3;
    --paper:#ffffff;
    --blue:#1565b5;
    --blue-dark:#0c3f8a;
    --blue-light:#29a8e0;
    --green:#8dc63f;
    --ink:#3a4654;
    --mute:#8a95a2;
    --ring:#e3ecd2;
  }
  *{box-sizing:border-box;margin:0;padding:0}
  html,body{width:1200px;height:799px;overflow:hidden}
  body{background:var(--bg);font-family:"Montserrat",Arial,sans-serif;color:var(--ink);position:relative}
  .piece{position:absolute;background:var(--paper);box-shadow:0 4px 14px rgba(0,0,0,.12);overflow:hidden}
  .band{position:absolute;left:0;bottom:0;width:100%;display:block}

  .brand{display:flex;align-items:center;gap:8px}
  .brand-dot{border-radius:50%;background:var(--green);flex:none}
  .brand-name{font-weight:800;color:var(--blue);text-transform:uppercase;line-height:1.1;letter-spacing:.02em}

  /* Letterhead */
  .letterhead{left:40px;top:40px;width:340px;height:440px}
  .letterhead .brand{position:absolute;left:26px;top:26px}
  .letterhead .brand-dot{width:20px;height:20px}
  .letterhead .brand-name{font-size:11px}
  .letterhead .watermark{position:absolute;left:80px;top:130px;width:180px;height:180px;border-radius:50%;border:3px solid var(--ring);background:radial-gradient(circle,#f4f8fc 0%,#fff 70%)}
  .letterhead .footer-line{position:absolute;left:26px;bottom:36px;font-size:8px;line-height:1.5;color:var(--mute);letter-spacing:.02em}

  /* Presentation folder */
  .folder{left:410px;top:40px;width:360px;height:440px}
  .folder .brand{position:absolute;left:0;right:0;top:150px;flex-direction:column;gap:14px;text-align:center}
  .folder .brand-dot{width:64px;height:64px}
  .folder .brand-name{font-size:24px}

  /* Envelope */
  .envelope{left:800px;top:40px;width:360px;height:170px}
  .envelope .brand{position:absolute;left:22px;top:20px}
  .envelope .brand-dot{width:18px;height:18px}
  .envelope .brand-name{font-size:10px}
  .envelope .return{position:absolute;left:22px;top:56px;font-size:8px;line-height:1.5;color:var(--mute)}

  /* Cards */
  .card{width:360px;height:200px}
  .card-front{left:800px;top:240px}
  .card-front .brand{position:absolute;left:20px;top:18px}
  .card-front .brand-dot{width:22px;height:22px}
  .card-front .brand-name{font-size:12px}
  .card-front .person{position:absolute;left:20px;top:62px}
  .card-front .person-name{font-size:18px;font-weight:800;color:var(--blue-dark)}
  .card-front .person-title{font-size:11px;font-weight:600;color:var(--blue);margin-top:2px}
  .card-front .contact{position:absolute;left:20px;top:112px;font-size:10.5px;line-height:1.45;color:var(--ink)}

  .card-back{left:800px;top:470px;background:linear-gradient(135deg,var(--blue-light),var(--blue) 55%,var(--blue-dark))}
  .card-back .brand{position:absolute;inset:0;justify-content:center;gap:10px}
  .card-back .brand-dot{width:28px;height:28px}
  .card-back .brand-name,.sleeve .brand-name,.disc .brand-name{color:#fff;font-size:14px}

  /* Disc and sleeve */
  .disc{position:absolute;left:40px;top:510px;width:240px;height:240px;border-radius:50%;background:radial-gradient(circle at 35% 30%,var(--blue-light),var(--blue) 55%,var(--blue-dark));box-shadow:0 4px 14px rgba(0,0,0,.15)}
  .disc .hole{position:absolute;left:50%;top:50%;width:44px;height:44px;margin:-22px 0 0 -22px;border-radius:50%;background:var(--bg);border:9px solid #fff}
  .disc .brand-name{position:absolute;left:0;right:0;top:160px;text-align:center;font-size:11px}
  .sleeve{left:310px;top:510px;width:240px;height:240px;background:linear-gradient(135deg,var(--blue-light),var(--blue) 55%,var(--blue-dark))}
  .sleeve .brand{position:absolute;inset:0;justify-content:center;flex-direction:column;gap:12px;text-align:center}
  .sleeve .brand-dot{width:36px;height:36px}
</style>
</head>
<body>

<section class="piece letterhead" aria-label="Letterhead">
  <div class="brand"><span class="brand-dot"></span><span class="brand-name">Bright Harbor<br>Associates</span></div>
  <div class="watermark"></div>
  <p class="footer-line">4780 W. Meadow Rd · State College, PA 16934<br>www.brightharborpa.example</p>
  <svg class="band" viewBox="0 0 340 22" height="22" preserveAspectRatio="none">
    <defs><linearGradient id="bandA" x1="0" x2="1"><stop offset="0" stop-color="#0c3f8a"/><stop offset="1" stop-color="#29a8e0"/></linearGradient></defs>
    <rect width="340" height="22" fill="url(#bandA)"/>
    <polygon points="268,22 296,0 340,0 340,22" fill="#8dc63f"/>
  </svg>
</section>

<section class="piece folder" aria-label="Presentation folder">
  <div class="brand"><span class="brand-dot"></span><span class="brand-name">Bright Harbor<br>Associates</span></div>
  <svg class="band" viewBox="0 0 360 24" height="24" preserveAspectRatio="none">
    <defs><linearGradient id="bandF" x1="0" x2="1"><stop offset="0" stop-color="#0c3f8a"/><stop offset="1" stop-color="#29a8e0"/></linearGradient></defs>
    <rect width="360" height="24" fill="url(#bandF)"/>
    <polygon points="280,24 310,0 360,0 360,24" fill="#8dc63f"/>
  </svg>
</section>

<section class="piece envelope" aria-label="Envelope">
  <div class="brand"><span class="brand-dot"></span><span class="brand-name">Bright Harbor<br>Associates</span></div>
  <p class="return">4780 W. Meadow Rd<br>State College, PA 16934</p>
  <svg class="band" viewBox="0 0 360 16" height="16" preserveAspectRatio="none">
    <defs><linearGradient id="bandB" x1="0" x2="1"><stop offset="0" stop-color="#0c3f8a"/><stop offset="1" stop-color="#29a8e0"/></linearGradient></defs>
    <rect width="360" height="16" fill="url(#bandB)"/>
    <polygon points="288,16 306,0 360,0 360,16" fill="#8dc63f"/>
  </svg>
</section>

<section class="piece card card-front" aria-label="Business card front">
  <div class="brand"><span class="brand-dot"></span><span class="brand-name">Bright Harbor Associates</span></div>
  <div class="person">
    <p class="person-name">Neil Vardakian</p>
    <p class="person-title">Senior Account Executive</p>
  </div>
  <p class="contact">4780 W. Meadow Rd, State College, PA 16934<br>neil@brightharborpa.example<br>www.brightharborpa.example</p>
  <svg class="band" viewBox="0 0 360 14" height="14" preserveAspectRatio="none">
    <defs><linearGradient id="bandC" x1="0" x2="1"><stop offset="0" stop-color="#0c3f8a"/><stop offset="1" stop-color="#29a8e0"/></linearGradient></defs>
    <rect width="360" height="14" fill="url(#bandC)"/>
    <polygon points="288,14 304,0 360,0 360,14" fill="#8dc63f"/>
  </svg>
</section>

<section class="piece card card-back" aria-label="Business card back">
  <div class="brand"><span class="brand-dot"></span><span class="brand-name">Bright Harbor Associates</span></div>
</section>

<section class="disc" aria-label="Disc label">
  <span class="hole"></span>
  <span class="brand-name">Bright Harbor Associates</span>
</section>

<section class="piece sleeve" aria-label="Disc sleeve">
  <div class="brand"><span class="brand-dot"></span><span class="brand-name">Bright Harbor<br>Associates</span></div>
</section>

</body>
</html>
```